Business card and (possibly) logo

Hi - we need a new business card.
We have an existing logo that we quite like but we are open to options.
We are an architectural firm - we specialize in upmarket residential work and apartment blocks.
We are chasing a business card at present but also want to extensively update our website going forward to attract a much higher level of client / investor / developer.
Our current logo is black, grey and yellow and based on the sun/moon temples in Mexico.
We are open to variations.
We want to communicate professionalism, trust, quality.
Our website is www.corvelldesignhouse.com.au - but note as above - we want to change the website as well to be a lot 'classier' and to appeal to a higher end market.

thanks

Target Market(s)

We are an architect firm - our target market is Developers and builders of high end houses and luxury apartment blocks. Also private home owners wanting to build excellent expensive houses. (ideally over $1m budgets)

Industry/Entity Type

Residential

Requirements
Must have
• Logo
Contact details;
Name
phone, mobile, email, web

```html
<!DOCTYPE html>
<html lang="en">
<head>
<meta charset="utf-8">
<title>Corvell Design House – Business Card</title>
<link rel="stylesheet" href="https://fonts.googleapis.com/css2?family=Arimo:wght@400;700&display=swap">
<style>
  :root {
    --backdrop: #d4d4d4;
    --card-white: #ffffff;
    --brand-orange: #f2a426;
    --ink: #111111;
    --ink-soft: #2a2a2a;
    --paper-line: #fdf1dc;
  }
  * { box-sizing: border-box; margin: 0; padding: 0; }
  html, body { width: 1200px; height: 985px; overflow: hidden; }
  body {
    background: radial-gradient(ellipse at 50% 40%, #e6e6e6 0%, var(--backdrop) 100%);
    font-family: "Arimo", Arial, sans-serif;
    position: relative;
  }
  .card {
    position: absolute;
    left: 320px;
    width: 560px;
    height: 350px;
    border-radius: 22px;
    overflow: hidden;
    box-shadow: 0 10px 26px rgba(0,0,0,0.22);
  }
  /* Front */
  .card-front { top: 95px; background: var(--card-white); }
  .front-brand {
    position: absolute;
    right: 48px;
    top: 150px;
    display: flex;
    align-items: center;
    gap: 12px;
  }
  .brand-dot {
    width: 22px; height: 22px; border-radius: 50%;
    background: var(--brand-orange);
  }
  .brand-name {
    font-weight: 700;
    font-size: 30px;
    letter-spacing: 1px;
    text-transform: uppercase;
    color: var(--ink);
    line-height: 1;
  }
  .web-band {
    position: absolute;
    right: 0; bottom: 0;
    width: 350px; height: 58px;
    background: var(--brand-orange);
    border-top-left-radius: 22px;
    display: flex;
    align-items: center;
    padding-left: 26px;
    gap: 14px;
  }
  .web-band svg { width: 22px; height: 22px; }
  .web-address {
    font-size: 17px;
    letter-spacing: 3.5px;
    color: var(--ink);
  }
  /* Back */
  .card-back { top: 535px; background: var(--brand-orange); }
  .identity {
    position: absolute;
    left: 0; top: 28px;
    width: 230px;
    padding-left: 60px;
    padding-bottom: 8px;
    border-bottom: 1px solid var(--paper-line);
  }
  .person-name { font-size: 24px; color: var(--ink); letter-spacing: 0.5px; }
  .person-role { font-size: 19px; color: var(--ink); letter-spacing: 0.5px; margin-top: 2px; }
  .contact-tab {
    position: absolute;
    left: -14px; top: 108px;
    width: 38px; height: 124px;
    background: var(--card-white);
    border-radius: 0 19px 19px 0;
    display: flex; flex-direction: column; align-items: flex-end;
    justify-content: space-around;
    padding: 8px 9px 8px 0;
  }
  .contact-tab span { font-size: 15px; color: var(--ink); line-height: 1; }
  .contact-list {
    position: absolute;
    left: 44px; top: 114px;
    list-style: none;
  }
  .contact-list li {
    font-size: 17px;
    line-height: 24.5px;
    color: var(--ink-soft);
    letter-spacing: 1.6px;
  }
  .back-brand {
    position: absolute;
    right: 44px; bottom: 56px;
    display: flex; align-items: center; gap: 12px;
  }
  .back-brand .brand-name { color: var(--card-white); font-size: 32px; }
  .back-brand .brand-dot { background: var(--card-white); }
</style>
</head>
<body>
  <section class="card card-front" aria-label="Card front">
    <div class="front-brand">
      <span class="brand-dot"></span>
      <span class="brand-name">Corvell Design House</span>
    </div>
    <div class="web-band">
      <svg viewBox="0 0 24 24" fill="none" stroke="#ffffff" stroke-width="1.6" aria-hidden="true">
        <circle cx="12" cy="12" r="10"/>
        <ellipse cx="12" cy="12" rx="4.5" ry="10"/>
        <line x1="2" y1="12" x2="22" y2="12"/>
        <line x1="4" y1="7" x2="20" y2="7"/>
        <line x1="4" y1="17" x2="20" y2="17"/>
      </svg>
      <span class="web-address">www.yourwebsite.com</span>
    </div>
  </section>

  <section class="card card-back" aria-label="Card back">
    <div class="identity">
      <p class="person-name">Your Name</p>
      <p class="person-role">Director</p>
    </div>
    <div class="contact-tab" aria-hidden="true">
      <span>T</span><span>M</span><span>E</span><span>W</span><span>A</span>
    </div>
    <ul class="contact-list">
      <li>020 7461 3058</li>
      <li>07812 604 275</li>
      <li>Youremail@email.com</li>
      <li>www.yourwebsite.com</li>
      <li>213 your address, Your address</li>
    </ul>
    <div class="back-brand">
      <span class="brand-dot"></span>
      <span class="brand-name">Corvell Design House</span>
    </div>
  </section>
</body>
</html>
```